Book Cover Design: Manuscript Mason's™ Roadmap: Indie-Release Essentials

I need a book cover designed for the first book in the "Manuscript Mason's™ Roadmap" series. Second book to follow in a few weeks and then we'll be rolling out 1-2 new titles per month throughout 2017.

The cover design should be something that can be replicated with a new subtitle, for the next books in the series.

The graphic designer’s work that is selected for my cover series will be given credit on the copyright page of the book(s).

Target Market(s)

Authors interested in self-publishing. Publishing.

Industry/Entity Type

Publishing

Font styles to use
Serif

Requirements
Must have
• Please see attached design instructions.
Nice to have
Should not have
• Cheesy book cover images on the cover.

```html
<!DOCTYPE html>
<html lang="en">
<head>
<meta charset="utf-8">
<title>Manuscript Mason's™ Roadmap: Indie-Release Essentials</title>
<link rel="stylesheet" href="https://fonts.googleapis.com/css2?family=Antonio:wght@300;400;600&family=Courier+Prime:wght@700&display=swap">
<style>
  :root {
    --backdrop: #e4e4e4;
    --cover-top: #c9e6ec;
    --cover-mid: #c2e1e8;
    --cover-low: #b8dbe3;
    --ink: #4a5a61;
    --band: #9dbec6;
    --plan-light: #c4e1e8;
    --plan-dark: #aacdd6;
    --machine-light: #bcdfe7;
    --machine-mid: #98c6d2;
    --machine-dark: #2f3438;
    --stamp: #47525a;
  }
  * { margin: 0; padding: 0; box-sizing: border-box; }
  html, body { width: 900px; height: 1200px; overflow: hidden; }
  body { background: var(--backdrop); position: relative; }

  .cover {
    position: absolute;
    left: 88px; top: 32px;
    width: 748px; height: 1124px;
    overflow: hidden;
    background: linear-gradient(180deg, var(--cover-top) 0%, var(--cover-mid) 50%, var(--cover-low) 100%);
    box-shadow: 0 2px 8px rgba(0,0,0,0.18);
  }

  .floor-plan-art {
    position: absolute;
    left: 0; top: 0;
    width: 748px; height: 433px;
    background: linear-gradient(180deg, var(--plan-dark) 0%, var(--plan-light) 100%);
    opacity: 0.75;
  }

  .title-band {
    position: absolute;
    top: 436px; height: 22px;
    background: var(--band);
  }
  .title-band--left { left: 0; width: 108px; }
  .title-band--right { left: 442px; width: 306px; }

  .series-title {
    position: absolute;
    left: 117px; top: 214px;
    font-family: "Antonio", "Oswald", sans-serif;
    font-weight: 600;
    font-size: 86px;
    line-height: 90px;
    color: var(--ink);
    letter-spacing: 0.5px;
  }
  .series-title .tm {
    font-size: 22px;
    vertical-align: top;
    position: relative;
    top: -28px;
    margin-left: 2px;
  }

  .subtitle {
    position: absolute;
    left: 118px; top: 612px;
    font-family: "Antonio", "Oswald", sans-serif;
    font-weight: 300;
    font-size: 31px;
    letter-spacing: 0.6px;
    color: var(--ink);
  }

  .typewriter-art {
    position: absolute;
    left: 0; top: 798px;
    width: 748px; height: 326px;
    background: linear-gradient(180deg,
      #b7bcbf 0%, #d9dcde 4%, #9ea3a6 8%,
      var(--machine-light) 12%, var(--machine-mid) 50%,
      #5a6f76 62%, var(--machine-dark) 75%, #56585a 100%);
  }

  .author {
    position: absolute;
    left: 0; top: 893px;
    width: 748px;
    text-align: center;
    font-family: "Courier Prime", "Courier New", monospace;
    font-weight: 700;
    font-size: 25px;
    letter-spacing: 1px;
    color: var(--stamp);
  }
</style>
</head>
<body>
  <main class="cover">
    <div class="floor-plan-art" role="img" aria-label="Faint architectural floor plan drawing in pale blue lines"></div>

    <div class="title-band title-band--left"></div>
    <div class="title-band title-band--right"></div>

    <h1 class="series-title">Manuscript<br>Mason's<span class="tm">TM</span><br>Roadmap</h1>

    <p class="subtitle">Indie-Release Essentials</p>

    <div class="typewriter-art" role="img" aria-label="Close-up of a pale blue vintage typewriter with its chrome paper bail and platen"></div>

    <p class="author">Marlene T. Okonski</p>
  </main>
</body>
</html>
```